Your Joint Helper - Orthopedic needs from one site

We need slides that help to educate users, interest investors and allow the complexity of the entire continuum of care to be explained so anyone can understand. Your Joint Helper is a Varomin Health Company. Yourjointhelperhub.example. We allow people to evaluate, educate and engage with providers from one site. Simplyfying orthopedic care and wellness from one site. Patients, doctors, personal trainers, therapist, nutritionist, yoga, gyms, athletic trainers and more can connect from one site

Target Market(s)

Investors, Patients, Doctors and wellness providers

Industry/Entity Type

Healthcare

Requirements
Must have
• Investor slides, sales slides, education, process....

```html
<!DOCTYPE html>
<html lang="en">
<head>
<meta charset="utf-8">
<title>Your Joint Helper – Presentation Deck</title>
<link rel="stylesheet" href="https://fonts.googleapis.com/css2?family=Ubuntu:wght@300;400;500;700&display=swap">
<style>
  :root{
    --navy:#0b2c66;
    --navy-deep:#081f4d;
    --blue:#2f7fd0;
    --blue-bright:#1f6fd6;
    --green:#7cc242;
    --orange:#e07a0c;
    --ink:#1d2a44;
    --text:#3a4458;
    --muted:#6b7385;
    --page:#d9d9db;
    --white:#ffffff;
  }
  *{box-sizing:border-box;margin:0;padding:0}
  html,body{width:1200px;height:2422px;overflow:hidden}
  body{
    position:relative;
    background:var(--page);
    font-family:"Ubuntu",Arial,sans-serif;
    color:var(--text);
  }
  .showcase{
    position:absolute;left:0;top:0;width:1200px;height:715px;
    background:linear-gradient(180deg,#c9ccd3 0%,#e4e5e8 60%,var(--page) 100%);
  }
  .brand-mark{
    position:absolute;left:905px;top:62px;
    display:flex;align-items:center;gap:12px;
    font-weight:500;font-size:30px;line-height:1.05;color:var(--navy);
    letter-spacing:.5px;text-transform:uppercase;
  }
  .brand-mark .dot{width:20px;height:20px;border-radius:50%;background:var(--green)}

  .slide{
    position:absolute;width:562px;height:316px;overflow:hidden;background:var(--white);
  }
  .hero{left:80px;top:140px;transform:scale(1.35);transform-origin:0 0;box-shadow:0 18px 40px rgba(10,30,70,.25)}
  .col-l{left:28px}.col-r{left:609px}
  .row-1{top:734px}.row-2{top:1070px}.row-3{top:1405px}.row-4{top:1740px}.row-5{top:2075px}

  .abs{position:absolute}
  .band{
    position:absolute;left:0;width:562px;
    background:radial-gradient(circle at 65% 40%,#1d5fb8 0%,#0f3a84 40%,var(--navy-deep) 100%);
  }
  .band-cover{top:82px;height:205px}
  .wordmark{
    position:absolute;display:flex;align-items:center;gap:6px;
    font-weight:500;color:var(--navy);text-transform:uppercase;line-height:1.05;
  }
  .wordmark .dot{border-radius:50%;background:var(--green);flex:none}
  .wordmark-lg{left:46px;top:24px;font-size:13px}
  .wordmark-lg .dot{width:10px;height:10px}
  .wordmark-sm{left:12px;bottom:12px;font-size:7px}
  .wordmark-sm .dot{width:6px;height:6px}
  .wordmark-sm.on-dark{color:var(--white)}

  .kicker{position:absolute;left:45px;top:128px;color:var(--white);font-weight:300;font-size:13.5px}
  .cover-title{position:absolute;left:45px;top:150px;color:var(--green);font-weight:400;font-size:25px;line-height:1.15;text-transform:uppercase}
  .date-pill{
    position:absolute;left:45px;top:228px;width:110px;height:19px;border-radius:10px;
    background:var(--orange);color:var(--white);font-size:6.3px;font-weight:500;
    display:flex;align-items:center;justify-content:center;
  }
  .copyright{position:absolute;left:0;right:0;top:298px;text-align:center;font-size:5px;color:var(--muted)}
  .photo{position:absolute}
  .photo-person{left:340px;top:82px;width:222px;height:205px;background:linear-gradient(160deg,#1b8f9c 0%,#2bb3b0 45%,#12507e 100%)}
  .page-no{
    position:absolute;right:12px;bottom:14px;width:11px;height:11px;border-radius:50%;
    background:var(--blue-bright);color:var(--white);font-size:5.5px;
    display:flex;align-items:center;justify-content:center;
  }
  .heading{font-weight:400;text-transform:uppercase;color:var(--navy);font-size:19px;line-height:1.1}
  .heading-light{color:var(--white)}
  .sub-green{color:var(--green);font-size:10px;text-transform:uppercase;font-weight:400}
  .sub-blue{color:var(--blue);font-size:9px;text-transform:uppercase}
  .body{font-size:5.5px;line-height:1.3;color:var(--text)}
  .bullets{list-style:none;font-size:5.5px;line-height:1.35;color:var(--text)}
  .bullets li{position:relative;padding-left:8px;margin-bottom:2px}
  .bullets li::before{content:"";position:absolute;left:0;top:2px;width:3px;height:3px;border-radius:50%;background:var(--green)}
  .bullets.sq li::before{border-radius:0;background:var(--blue)}
  .img-med{background:linear-gradient(135deg,#1f4f8a 0%,#6ea9d6 55%,#d6e8f3 100%)}
  .img-lab{background:linear-gradient(135deg,#bfe0ee 0%,#6fb8d4 50%,#eaf4f8 100%)}
  .img-tech{background:linear-gradient(135deg,#0d3a78 0%,#2f78c0 60%,#8cc1e6 100%)}
  .icon{position:absolute;width:22px;height:22px;border-radius:50%;display:flex;align-items:center;justify-content:center}
  .icon svg{width:12px;height:12px}
  .bg-green{background:var(--green)}.bg-blue{background:var(--blue)}.bg-navy{background:var(--navy)}
  .feature-title{position:absolute;font-size:6.5px;color:var(--green);text-transform:uppercase}
  .feature-text{position:absolute;font-size:5px;line-height:1.3;color:var(--text);width:92px}
  .center{text-align:center}
</style>
</head>
<body>

<section class="showcase">
  <div class="brand-mark"><span class="dot"></span><span>Your Joint<br>Helper</span></div>

  <article class="slide hero">
    <div class="wordmark wordmark-lg"><span class="dot"></span><span>Your Joint<br>Helper</span></div>
    <div class="band band-cover"></div>
    <div class="photo photo-person" role="img" aria-label="Smiling doctor in teal scrubs with stethoscope, arms crossed"></div>
    <p class="kicker">Simplifying Your Orthopedic Care</p>
    <h1 class="cover-title">Evaluate, Edducate<br>&amp; Engage</h1>
    <div class="date-pill">Thursday, October 6, 2022</div>
    <p class="copyright">Copyright © 2022 Your Joint Helper</p>
  </article>
</section>

<!-- Row 1 -->
<article class="slide col-l row-1">
  <div class="wordmark wordmark-lg"><span class="dot"></span><span>Your Joint<br>Helper</span></div>
  <div class="band band-cover"></div>
  <div class="photo photo-person" role="img" aria-label="Smiling doctor in teal scrubs with stethoscope, arms crossed"></div>
  <p class="kicker">Simplifying Your Orthopedic Care</p>
  <h2 class="cover-title">Evaluate, Edducate<br>&amp; Engage</h2>
  <div class="date-pill">Thursday, October 6, 2022</div>
  <p class="copyright">Copyright © 2022 Your Joint Helper</p>
</article>

<article class="slide col-r row-1">
  <div class="wordmark wordmark-lg"><span class="dot"></span><span>Your Joint<br>Helper</span></div>
  <div class="band band-cover"></div>
  <div class="photo photo-person" role="img" aria-label="Doctor in teal scrubs holding a stethoscope, cropped at the shoulders"></div>
  <p class="kicker">Simplifying Your Orthopedic Care</p>
  <h2 class="cover-title">Evaluate, Edducate<br>&amp; Engage</h2>
  <div class="date-pill">Thursday, October 6, 2022</div>
  <p class="copyright">Copyright © 2022 Your Joint Helper</p>
</article>

<!-- Row 2 -->
<article class="slide col-l row-2">
  <div class="wordmark wordmark-lg"><span class="dot"></span><span>Your Joint<br>Helper</span></div>
  <div class="band band-cover"></div>
  <p class="kicker">Your Joint Helper</p>
  <h2 class="cover-title">Presentation<br>Title Goes Here</h2>
  <div class="date-pill">Thursday, October 6, 2022</div>
  <p class="copyright">Copyright © 2022 Your Joint Helper</p>
</article>

<article class="slide col-r row-2">
  <h2 class="heading abs" style="left:40px;top:40px;width:270px;font-size:20px">Lorem ipsum dolor sit amet consectetur.</h2>
  <ul class="bullets sq abs" style="left:40px;top:105px;width:270px">
    <li>Lorem ipsum dolor sit amet, consectetur adipiscing elit. Vivamus eu dui ex. Curabitur dapibus dignissim dui, in molestie metus feugiat sed.</li>
    <li>Lorem ipsum dolor sit amet, consectetur adipiscing elit. Vivamus eu dui ex. Curabitur dapibus dignissim dui, in molestie metus feugiat sed. Praesent aliquet lorem ex, eu dapibus odio varius at. Lorem ipsum dolor sit amet, consectetur adipiscing elit. Vivamus eu dui ex. Curabitur dapibus dignissim dui, in molestie metus feugiat sed. Praesent aliquet lorem ex, eu dapibus odio varius at.</li>
    <li>Lorem ipsum dolor sit amet, consectetur adipiscing elit. Vivamus eu dui ex. Curabitur dapibus dignissim dui, in molestie metus feugiat sed. Praesent aliquet lorem ex, eu dapibus odio varius at.</li>
  </ul>
  <p class="body abs" style="left:40px;top:235px;width:270px;font-size:4.8px">Lorem ipsum dolor sit amet, consectetur adipiscing elit. Vivamus eu dui ex. Curabitur dapibus dignissim dui, in molestie metus feugiat sed.</p>
  <div class="photo img-tech" style="left:331px;top:0;width:207px;height:262px" role="img" aria-label="Hand with stethoscope over a laptop with a glowing digital brain graphic"></div>
  <div class="wordmark wordmark-sm"><span class="dot"></span><span>Your Joint<br>Helper</span></div>
  <div class="page-no">4</div>
</article>

<!-- Row 3 -->
<article class="slide col-l row-3">
  <div class="band" style="top:0;height:98px"></div>
  <h2 class="heading heading-light abs center" style="left:0;right:0;top:24px">Heading goes here</h2>
  <div class="photo img-med" style="left:31px;top:72px;width:245px;height:71px" role="img" aria-label="Doctor with stethoscope reviewing a digital tablet"></div>
  <div class="photo img-lab" style="left:286px;top:72px;width:245px;height:71px" role="img" aria-label="Medical professional working with digital health interface"></div>
  <h3 class="sub-green abs" style="left:36px;top:160px">Heading goes here</h3>
  <p class="body abs" style="left:36px;top:175px;width:232px">Lorem ipsum dolor sit amet, consectetur adipiscing elit. Vivamus eu dui ex. Curabitur dapibus dignissim dui, in molestie metus feugiat sed. Praesent aliquet lorem ex, eu dapibus odio varius at.</p>
  <ul class="bullets abs" style="left:36px;top:218px;width:232px">
    <li>Lorem ipsum dolor sit amet, consectetur adipiscing elit.</li>
    <li>Vivamus eu dui ex. Curabitur dapibus dignissim dui, in molestie</li>
    <li>Praesent aliquet lorem ex, eu dapibus odio varius at.</li>
    <li>Duis eget tellus porta, consequat lacus vitae, venenatis dolor.</li>
  </ul>
  <h3 class="sub-green abs" style="left:291px;top:160px">Heading goes here</h3>
  <p class="body abs" style="left:291px;top:175px;width:232px">Lorem ipsum dolor sit amet, consectetur adipiscing elit. Vivamus eu dui ex. Curabitur dapibus dignissim dui, in molestie metus feugiat sed. Praesent aliquet lorem ex, eu dapibus odio varius at.</p>
  <ul class="bullets abs" style="left:291px;top:218px;width:232px">
    <li>Lorem ipsum dolor sit amet, consectetur adipiscing elit.</li>
    <li>Vivamus eu dui ex. Curabitur dapibus dignissim dui, in molestie</li>
    <li>Praesent aliquet lorem ex, eu dapibus odio varius at.</li>
    <li>Duis eget tellus porta, consequat lacus vitae, venenatis dolor.</li>
  </ul>
  <div class="wordmark wordmark-sm"><span class="dot"></span><span>Your Joint<br>Helper</span></div>
  <div class="page-no">5</div>
</article>

<article class="slide col-r row-3">
  <h2 class="heading abs" style="left:35px;top:32px">Heading goes here</h2>
  <div class="band" style="top:77px;width:282px;height:119px;background:var(--navy)"></div>
  <div class="icon bg-blue" style="left:22px;top:92px"><svg viewBox="0 0 24 24" fill="#fff"><path d="M12 2a7 7 0 0 0-4 12.7V17h8v-2.3A7 7 0 0 0 12 2zM9 19h6v2H9z"/></svg></div>
  <p class="abs" style="left:75px;top:92px;color:#fff;font-size:7.5px">TITLE GOES HERE</p>
  <p class="abs" style="left:75px;top:103px;width:190px;color:#cfd8ea;font-size:4.8px;line-height:1.3">Lorem ipsum dolor sit amet, consectetur adipiscing elit. Vivamus eu dui ex. Curabitur dapibus dignissim dui, in molestie metus feugiat sed.</p>
  <div class="icon bg-green" style="left:22px;top:144px"><svg viewBox="0 0 24 24" fill="#fff"><path d="M4 20h3v-6H4zm6 0h3V10h-3zm6 0h3V5h-3z"/></svg></div>
  <p class="abs" style="left:75px;top:143px;color:#fff;font-size:7.5px">TITLE GOES HERE</p>
  <p class="abs" style="left:75px;top:154px;width:190px;color:#cfd8ea;font-size:4.8px;line-height:1.3">Lorem ipsum dolor sit amet, consectetur adipiscing elit. Vivamus eu dui ex. Curabitur dapibus dignissim dui, in molestie metus feugiat sed.</p>
  <div class="photo img-lab" style="left:282px;top:77px;width:280px;height:119px" role="img" aria-label="Doctor in white coat using a digital tablet in a bright hospital corridor"></div>
  <h3 class="sub-blue abs" style="left:27px;top:209px">Title goes here</h3>
  <p class="body abs" style="left:27px;top:222px;width:235px;font-size:5px">Lorem ipsum dolor sit amet, consectetur adipiscing elit. Vivamus eu dui ex. Curabitur dapibus dignissim dui, in molestie metus feugiat sed. Praesent aliquet lorem ex, eu dapibus odio varius at. Lorem ipsum dolor sit amet, consectetur adipiscing elit. Vivamus eu dui ex. Curabitur dapibus dignissim dui, in molestie metus feugiat sed.</p>
  <h3 class="sub-blue abs" style="left:300px;top:209px">Title goes here</h3>
  <p class="body abs" style="left:300px;top:222px;width:235px;font-size:5px">Lorem ipsum dolor sit amet, consectetur adipiscing elit. Vivamus eu dui ex. Curabitur dapibus dignissim dui, in molestie metus feugiat sed. Praesent aliquet lorem ex, eu dapibus odio varius at. Lorem ipsum dolor sit amet, consectetur adipiscing elit. Vivamus eu dui ex.</p>
  <div class="wordmark wordmark-sm"><span class="dot"></span><span>Your Joint<br>Helper</span></div>
  <div class="page-no">6</div>
</article>

<!-- Row 4 -->
<article class="slide col-l row-4">
  <div class="band" style="top:0;width:193px;height:316px"></div>
  <h2 class="heading heading-light abs" style="left:34px;top:72px">Heading<br>goes here</h2>
  <p class="abs" style="left:34px;top:137px;width:135px;color:#fff;font-size:5.5px;line-height:1.3">Lorem ipsum dolor sit amet, consectetur adipiscing elit. Vivamus eu dui ex. Curabitur dapibus dignissim dui, in molestie metus feugiat sed. Praesent aliquet lorem ex, eu dapibus odio varius at. Duis eget tellus porta, consequat lacus vitae, venenatis dolor. Nulla facilisi. In et sollicitudin lacus.</p>
  <div class="wordmark wordmark-sm on-dark"><span class="dot"></span><span>Your Joint<br>Helper</span></div>

  <div class="icon bg-green" style="left:223px;top:68px;width:34px;height:34px"><svg viewBox="0 0 24 24" fill="#fff"><path d="M12 2a7 7 0 0 0-4 12.7V17h8v-2.3A7 7 0 0 0 12 2zM9 19h6v2H9z"/></svg></div>
  <p class="feature-title" style="left:266px;top:63px">Heading</p>
  <p class="feature-text" style="left:266px;top:73px">Praesent aliquet lorem ex, eu dapibus odio varius at. Duis eget tellus porta, consequat lacus vitae.</p>
  <div class="icon bg-blue" style="left:388px;top:68px;width:34px;height:34px"><svg viewBox="0 0 24 24" fill="#fff"><circle cx="8" cy="9" r="3"/><circle cx="16" cy="9" r="3"/><path d="M2 19c0-3 3-5 6-5s6 2 6 5zm10 0c0-3 2-5 4-5 3 0 6 2 6 5z"/></svg></div>
  <p class="feature-title" style="left:431px;top:63px">Heading</p>
  <p class="feature-text" style="left:431px;top:73px">Praesent aliquet lorem ex, eu dapibus odio varius at. Duis eget tellus porta, consequat lacus vitae.</p>

  <div class="icon bg-navy" style="left:223px;top:142px;width:34px;height:34px"><svg viewBox="0 0 24 24" fill="none" stroke="#fff" stroke-width="2"><rect x="4" y="5" width="16" height="15" rx="1"/><path d="M4 10h16M8 3v4M16 3v4M8 14h2M12 14h2M8 17h2M12 17h2"/></svg></div>
  <p class="feature-title" style="left:266px;top:137px">Heading</p>
  <p class="feature-text" style="left:266px;top:147px">Praesent aliquet lorem ex, eu dapibus odio varius at. Duis eget tellus porta, consequat lacus vitae.</p>
  <div class="icon bg-green" style="left:388px;top:142px;width:34px;height:34px"><svg viewBox="0 0 24 24" fill="#fff"><path d="M4 20h3v-5H4zm6 0h3v-8h-3zm6 0h3V8h-3zM4 11l6-5 4 3 6-5"/></svg></div>
  <p class="feature-title" style="left:431px;top:137px">Heading</p>
  <p class="feature-text" style="left:431px;top:147px">Praesent aliquet lorem ex, eu dapibus odio varius at. Duis eget tellus porta, consequat lacus vitae.</p>

  <div class="icon bg-blue" style="left:223px;top:216px;width:34px;height:34px"><svg viewBox="0 0 24 24" fill="none" stroke="#fff" stroke-width="2"><rect x="4" y="5" width="16" height="14" rx="1"/><path d="M7 9h10M7 12h10M7 15h6"/></svg></div>
  <p class="feature-title" style="left:266px;top:211px">Heading</p>
  <p class="feature-text" style="left:266px;top:221px">Praesent aliquet lorem ex, eu dapibus odio varius at. Duis eget tellus porta, consequat lacus vitae.</p>
  <div class="icon bg-navy" style="left:388px;top:216px;width:34px;height:34px"><svg viewBox="0 0 24 24" fill="#fff"><path d="M9 4h6v3h5v13H4V7h5zm2 2v1h2V6zm0 5v3H8v2h3v3h2v-3h3v-2h-3v-3z"/></svg></div>
  <p class="feature-title" style="left:431px;top:211px">Heading</p>
  <p class="feature-text" style="left:431px;top:221px">Praesent aliquet lorem ex, eu dapibus odio varius at. Duis eget tellus porta, consequat lacus vitae.</p>
  <div class="page-no">7</div>
</article>

<article class="slide col-r row-4">
  <div class="band" style="top:0;height:104px"></div>
  <h2 class="heading heading-light abs center" style="left:0;right:0;top:25px">Heading goes here</h2>
  <div class="photo img-tech" style="left:31px;top:72px;width:118px;height:71px" role="img" aria-label="Hands using a tablet showing a digital brain scan"></div>
  <div class="photo img-lab" style="left:158px;top:72px;width:118px;height:71px" role="img" aria-label="Clinician viewing translucent digital medical display"></div>
  <div class="photo img-med" style="left:286px;top:72px;width:118px;height:71px" role="img" aria-label="Hand reaching toward glowing health data interface"></div>
  <div class="photo img-lab" style="left:413px;top:72px;width:118px;height:71px" role="img" aria-label="Doctor working with a tablet in a bright clinic"></div>
  <h3 class="sub-green abs center" style="left:31px;top:160px;width:118px;line-height:1.2">Heading<br>goes here</h3>
  <p class="body abs center" style="left:36px;top:190px;width:108px;font-size:5px">Lorem ipsum dolor sit amet, consectetur adipiscing elit. Vivamus eu dui ex. Curabitur dapibus dignissim dui, in molestie metus feugiat sed. Praesent aliquet lorem ex, eu dapibus odio varius at. Duis eget tellus porta, consequat lacus.</p>
  <h3 class="sub-green abs center" style="left:158px;top:160px;width:118px;line-height:1.2">Heading<br>goes here</h3>
  <p class="body abs center" style="left:163px;top:190px;width:108px;font-size:5px">Lorem ipsum dolor sit amet, consectetur adipiscing elit. Vivamus eu dui ex. Curabitur dapibus dignissim dui, in molestie metus feugiat sed. Praesent aliquet lorem ex, eu dapibus odio varius at. Duis eget tellus porta, consequat lacus.</p>
  <h3 class="sub-green abs center" style="left:286px;top:160px;width:118px;line-height:1.2">Heading<br>goes here</h3>
  <p class="body abs center" style="left:291px;top:190px;width:108px;font-size:5px">Lorem ipsum dolor sit amet, consectetur adipiscing elit. Vivamus eu dui ex. Curabitur dapibus dignissim dui, in molestie metus feugiat sed. Praesent aliquet lorem ex, eu dapibus odio varius at. Duis eget tellus porta, consequat lacus.</p>
  <h3 class="sub-green abs center" style="left:413px;top:160px;width:118px;line-height:1.2">Heading<br>goes here</h3>
  <p class="body abs center" style="left:418px;top:190px;width:108px;font-size:5px">Lorem ipsum dolor sit amet, consectetur adipiscing elit. Vivamus eu dui ex. Curabitur dapibus dignissim dui, in molestie metus feugiat sed. Praesent aliquet lorem ex, eu dapibus odio varius at. Duis eget tellus porta, consequat lacus.</p>
  <div class="wordmark wordmark-sm"><span class="dot"></span><span>Your Joint<br>Helper</span></div>
  <div class="page-no">8</div>
</article>

<!-- Row 5 -->
<article class="slide col-l row-5">
  <h2 class="heading abs" style="left:35px;top:38px">Heading goes here</h2>
  <svg class="abs chart" style="left:40px;top:88px" width="300" height="130" viewBox="0 0 300 130" aria-label="Bar chart comparing three series across four categories">
    <g font-family="Ubuntu, Arial, sans-serif" font-size="5" fill="#555">
      <g stroke="#e3e5ea" stroke-width="0.6">
        <line x1="14" y1="10" x2="296" y2="10"/><line x1="14" y1="27" x2="296" y2="27"/>
        <line x1="14" y1="44" x2="296" y2="44"/><line x1="14" y1="61" x2="296" y2="61"/>
        <line x1="14" y1="78" x2="296" y2="78"/><line x1="14" y1="95" x2="296" y2="95"/>
      </g>
      <line x1="14" y1="112" x2="296" y2="112" stroke="#9aa0ab" stroke-width="0.6"/>
      <text x="6" y="14">6</text><text x="6" y="31">5</text><text x="6" y="48">4</text>
      <text x="6" y="65">3</text><text x="6" y="82">2</text><text x="6" y="99">1</text><text x="6" y="116">0</text>
      <rect x="28" y="39" width="10" height="73" fill="#2f7fd0"/>
      <rect x="40" y="71" width="10" height="41" fill="#7cc242"/>
      <rect x="52" y="78" width="10" height="34" fill="#0b2c66"/>
      <rect x="98" y="70" width="10" height="42" fill="#2f7fd0"/>
      <rect x="110" y="37" width="10" height="75" fill="#7cc242"/>
      <rect x="122" y="78" width="10" height="34" fill="#0b2c66"/>
      <rect x="168" y="53" width="10" height="59" fill="#2f7fd0"/>
      <rect x="180" y="82" width="10" height="30" fill="#7cc242"/>
      <rect x="192" y="61" width="10" height="51" fill="#0b2c66"/>
      <rect x="238" y="36" width="10" height="76" fill="#2f7fd0"/>
      <rect x="250" y="64" width="10" height="48" fill="#7cc242"/>
      <rect x="262" y="27" width="10" height="85" fill="#0b2c66"/>
      <text x="34" y="122">Category 1</text><text x="104" y="122">Category 2</text>
      <text x="174" y="122">Category 3</text><text x="244" y="122">Category 4</text>
    </g>
  </svg>
  <p class="body abs" style="left:48px;top:228px;width:275px;font-size:5px">Lorem ipsum dolor sit amet, consectetur adipiscing elit. Vivamus eu dui ex. Curabitur dapibus dignissim dui, in molestie metus feugiat sed. Praesent aliquet lorem ex, eu dapibus odio varius at. Lorem ipsum dolor sit amet, consectetur adipiscing elit. Vivamus eu dui ex. Curabitur dapibus dignissim dui, in molestie metus feugiat sed. Praesent aliquet lorem ex, eu dapibus odio varius at.</p>
  <span class="abs" style="left:358px;top:92px;width:10px;height:10px;background:var(--blue)"></span>
  <h3 class="abs" style="left:378px;top:92px;font-size:7.5px;color:var(--blue)">HEADING GOES HERE</h3>
  <p class="body abs" style="left:378px;top:104px;width:140px;font-size:5px">Lorem ipsum dolor sit amet, consectetur adipiscing elit. Vivamus eu dui ex. Curabitur dapibus dignissim dui, in molestie metus feugiat sed.</p>
  <span class="abs" style="left:358px;top:152px;width:10px;height:10px;background:var(--green)"></span>
  <h3 class="abs" style="left:378px;top:152px;font-size:7.5px;color:var(--green)">HEADING GOES HERE</h3>
  <p class="body abs" style="left:378px;top:164px;width:140px;font-size:5px">Lorem ipsum dolor sit amet, consectetur adipiscing elit. Vivamus eu dui ex. Curabitur dapibus dignissim dui, in molestie metus feugiat sed.</p>
  <span class="abs" style="left:358px;top:212px;width:10px;height:10px;background:var(--navy)"></span>
  <h3 class="abs" style="left:378px;top:212px;font-size:7.5px;color:var(--navy)">HEADING GOES HERE</h3>
  <p class="body abs" style="left:378px;top:224px;width:140px;font-size:5px">Lorem ipsum dolor sit amet, consectetur adipiscing elit. Vivamus eu dui ex. Curabitur dapibus dignissim dui, in molestie metus feugiat sed.</p>
  <div class="wordmark wordmark-sm"><span class="dot"></span><span>Your Joint<br>Helper</span></div>
  <div class="page-no">9</div>
</article>

<article class="slide col-r row-5">
  <div class="wordmark wordmark-lg"><span class="dot"></span><span>Your Joint<br>Helper</span></div>
  <div class="band band-cover"></div>
  <div class="photo photo-person" role="img" aria-label="Doctor in teal scrubs holding a stethoscope, cropped at the shoulders"></div>
  <h2 class="cover-title" style="top:120px">Thank you!</h2>
  <p class="abs" style="left:45px;top:172px;color:#fff;font-size:10px">Contact Us</p>
  <div class="abs" style="left:45px;top:195px;display:flex;flex-direction:column;gap:6px;color:#fff;font-size:5.5px">
    <span style="display:flex;align-items:center;gap:8px"><svg width="9" height="9" viewBox="0 0 24 24" fill="#fff"><path d="M6.6 10.8a15 15 0 0 0 6.6 6.6l2.2-2.2c.3-.3.7-.4 1-.2 1.1.4 2.3.6 3.6.6.6 0 1 .4 1 1V20c0 .6-.4 1-1 1A17 17 0 0 1 3 4c0-.6.4-1 1-1h3.5c.6 0 1 .4 1 1 0 1.3.2 2.5.6 3.6.1.3 0 .7-.2 1z"/></svg>Insert Phone Number</span>
    <span style="display:flex;align-items:center;gap:8px"><svg width="9" height="9" viewBox="0 0 24 24" fill="none" stroke="#fff" stroke-width="2.2"><circle cx="12" cy="12" r="4"/><path d="M16 8v5a3 3 0 0 0 6 0v-1a10 10 0 1 0-4 8"/></svg>Insert E-Mail Address</span>
    <span style="display:flex;align-items:center;gap:8px"><svg width="9" height="9" viewBox="0 0 24 24" fill="none" stroke="#fff" stroke-width="2"><circle cx="12" cy="12" r="9"/><path d="M3 12h18M12 3c3 3 3 15 0 18M12 3c-3 3-3 15 0 18"/></svg>Insert URL Address</span>
  </div>
  <p class="copyright">Copyright © 2022 Your Joint Helper</p>
</article>

</body>
</html>
```